Eyecatching Design for Car price comparison website - read now! :)

We need a cool fresh responsive design for our website www.fahrzeug-preis-finder.de ... it is a website where you can calculate the worth of your old used car for free.

We like the layout of http://www.wagenhandelplatz.de/ or https://www.qorm.de very much.

We want the customer to quickly understand how the website works and what he can do. The customer should develop trust to our calculation.

Our old Color green should be included.
Updates

Reason: Hey guys, some more designs are welcome... Now coded project! :)

Target Market(s)

People that want to sell their cars, men and women

Industry/Entity Type

Car Dealer

Coding

Coded - Design and coding required

Number of Pages Required

3 page

Font styles to use
Sans Serif

Colors
acd036

Requirements
Must have
• Attractive, Trusting, Responsive, Focus on functionality
Should not have
• To be to close to http://www.wagenhandelplatz.de/ or https://www.qorm.de

```html
<!DOCTYPE html>
<html lang="de">
<head>
<meta charset="utf-8">
<title>Fahrzeug Preis Finder – Kostenlose Autobewertung</title>
<link rel="stylesheet" href="https://fonts.googleapis.com/css2?family=Lato:wght@400;700;900&display=swap">
<style>
:root{
  --lime:#acd036;
  --lime-dark:#8aa825;
  --olive:#5b6b1e;
  --ink:#2b2b2b;
  --text:#3a3a3a;
  --muted:#777;
  --field:#ffffff;
  --panel:#e4e4e4;
  --footer:#ededed;
  --white:#fff;
}
*{margin:0;padding:0;box-sizing:border-box}
html,body{width:1200px;height:2432px;overflow:hidden}
body{position:relative;background:var(--white);font-family:'Lato',Arial,sans-serif;color:var(--text)}
.abs{position:absolute}

/* top contact strip */
.contact-strip{top:0;height:26px;display:flex;align-items:center;font-size:13px;color:var(--white)}
.contact-strip.mail{left:592px;width:270px;background:var(--lime);clip-path:polygon(22px 0,100% 0,100% 100%,0 100%);padding-left:20px;color:var(--ink)}
.contact-strip.phone{left:820px;width:380px;background:var(--ink);clip-path:polygon(22px 0,100% 0,100% 100%,0 100%);padding-left:36px;font-weight:700}
.contact-strip svg{margin-right:8px}

/* header */
.brand{left:162px;top:28px;display:flex;align-items:center;gap:12px}
.brand-dot{width:40px;height:40px;border-radius:50%;background:var(--lime)}
.brand-name{font-weight:700;font-size:20px;line-height:22px;color:var(--ink);letter-spacing:.5px}
.appointment{left:835px;top:44px;height:34px;width:203px;display:flex;align-items:center}
.appointment .icon{width:38px;height:38px;border-radius:50%;background:var(--lime);display:flex;align-items:center;justify-content:center;position:relative;z-index:1;border:3px solid var(--white)}
.appointment .label{margin-left:-8px;flex:1;height:30px;background:var(--lime);display:flex;align-items:center;justify-content:center;font-weight:700;font-size:15px;color:var(--ink)}

/* nav */
.main-nav{top:92px;left:0;width:1200px;height:36px;background:var(--lime)}
.main-nav ul{list-style:none;position:absolute;left:162px;width:876px;height:36px;display:flex;border-left:1px solid rgba(0,0,0,.15)}
.main-nav li{display:flex;align-items:center;justify-content:center;font-size:15px;font-weight:700;color:var(--ink);border-right:1px solid rgba(0,0,0,.15)}

/* hero */
.hero{top:128px;left:0;width:1200px;height:428px;background:linear-gradient(90deg,#d5d5d5 0%,#f2f2f2 35%,#e9e9e9 60%,#dcdcdc 100%)}
.hero-photo{position:absolute;left:0;top:0;width:650px;height:428px;background:radial-gradient(ellipse at 55% 55%,#fbfbfb 0%,#d9d9d9 55%,#bdbdbd 100%)}
.valuation{left:665px;top:173px;width:331px;height:345px;background:var(--panel)}
.ribbon{left:628px;top:190px;width:410px;height:37px}
.ribbon .band{position:absolute;left:24px;top:0;width:362px;height:37px;background:var(--lime);color:var(--ink);font-weight:900;font-size:11.5px;line-height:15px;text-align:center;padding-top:4px;text-transform:uppercase}
.ribbon .tail{position:absolute;top:8px;width:30px;height:30px;background:var(--lime-dark)}
.ribbon .tail.l{left:0;clip-path:polygon(0 0,100% 0,100% 100%,0 100%,10px 50%)}
.ribbon .tail.r{right:0;clip-path:polygon(0 0,100% 0,calc(100% - 10px) 50%,100% 100%,0 100%)}
.field-label{left:678px;font-size:11.5px;font-weight:700;color:var(--ink)}
.field{background:var(--field);height:35px;font-size:10.5px;color:#999;display:flex;align-items:center;padding-left:10px}
.field.select{justify-content:space-between;padding-right:14px}
.get-btn{left:665px;top:477px;width:331px;height:21px;background:var(--lime);font-size:12px;font-weight:900;color:var(--ink);display:flex;align-items:center;justify-content:center;letter-spacing:.3px}

/* dark band sections */
.car-value{top:556px;left:0;width:1200px;height:242px;border-top:3px solid var(--lime);background:linear-gradient(90deg,#1e1e1e 0%,#3a3733 30%,#2d2a27 60%,#151515 100%)}
.section-title{font-weight:900;font-size:26px;text-transform:uppercase;letter-spacing:.3px}
.section-title .accent{color:var(--lime)}
.car-value .section-title{position:absolute;top:48px;width:100%;text-align:center;color:var(--white)}
.car-value p{position:absolute;left:180px;width:840px;top:96px;text-align:center;font-size:12.5px;line-height:20px;color:#eee}
.read-more{background:var(--lime);color:var(--ink);font-size:10px;font-weight:700;padding:0 7px;height:20px;display:inline-flex;align-items:center}
.car-value .read-more{position:absolute;left:563px;top:174px}

/* features */
.features{top:798px;left:0;width:1200px;height:327px}
.feature{position:absolute;top:45px;width:240px;text-align:center}
.feature .ring{margin:0 auto;width:170px;height:170px;border-radius:50%;background:var(--lime);display:flex;align-items:center;justify-content:center;border:6px dashed #c4e06a}
.feature .core{width:132px;height:132px;border-radius:50%;background:var(--white);display:flex;align-items:center;justify-content:center}
.feature h3{margin-top:28px;font-size:19px;font-weight:400;line-height:26px;color:var(--ink)}

/* sell */
.sell{top:1125px;left:0;width:1200px;height:344px;background:linear-gradient(90deg,#151515 0%,#2c2c2c 45%,#3c3c3c 70%,#1d1d1d 100%)}
.sell-photo{position:absolute;left:730px;top:0;width:470px;height:344px;background:radial-gradient(ellipse at 60% 55%,#b3242a 0%,#6e1a1e 35%,#2e2a2a 70%,#1d1d1d 100%)}
.sell .section-title{position:absolute;left:162px;top:48px;color:var(--white)}
.sell h4{position:absolute;left:162px;top:87px;font-size:19px;font-weight:700;color:var(--white)}
.sell p{position:absolute;left:162px;top:118px;width:570px;font-size:12.3px;line-height:20.5px;color:#ddd}
.sell .read-more{position:absolute;left:162px;top:279px}

/* car list */
.car-list{top:1469px;left:0;width:1200px;height:365px}
.car-list .section-title{position:absolute;top:48px;width:100%;text-align:center;color:var(--ink)}
.make{position:absolute;width:127px;height:93px;border:1px solid #ddd;display:flex;align-items:center;justify-content:center;font-size:15px;font-weight:700;color:var(--ink);text-align:center;line-height:17px}

/* reviews */
.reviews{top:1834px;left:0;width:1200px;height:323px;background:linear-gradient(180deg,#1a2026 0%,#39424b 50%,#1a1f24 100%)}
.reviews .section-title{position:absolute;top:49px;width:100%;text-align:center;color:var(--white)}
.review{position:absolute;top:114px;height:141px;background:var(--white);display:flex;padding:7px}
.portrait{width:133px;height:127px;flex:none}
.review .body{padding:0 10px 0 12px}
.review p{font-size:10.5px;font-style:italic;line-height:16.5px;color:#666;margin-top:2px}
.stars{color:var(--lime);font-size:13px;letter-spacing:1px;margin-top:8px}
.stars .off{color:#ccc}
.review .name{font-size:12.5px;font-weight:700;color:var(--ink);margin-top:6px}
.arrow{position:absolute;top:171px;width:24px;height:24px;border:2px solid var(--white);display:flex;align-items:center;justify-content:center}

/* footer */
.site-footer{top:2157px;left:0;width:1200px;height:237px;background:var(--footer)}
.site-footer h5{font-size:14px;font-weight:900;color:var(--ink);text-transform:uppercase;padding-bottom:9px;border-bottom:1px solid #d3d3d3}
.quick-links{left:162px;top:40px;width:118px}
.quick-links ul{list-style:none;margin-top:10px}
.quick-links li{font-size:11.5px;line-height:21.5px;color:var(--ink);padding-left:14px;position:relative}
.quick-links li::before{content:"›";position:absolute;left:0;color:var(--muted)}
.contact-info{left:345px;top:40px;width:200px}
.contact-row{display:flex;gap:14px;font-size:11.5px;line-height:15px;color:var(--ink);margin-top:14px}
.contact-row svg{flex:none;margin-top:1px}
.news{left:618px;top:40px;width:220px}
.news-item{display:flex;gap:10px;margin-top:14px}
.date{width:32px;flex:none;text-align:center}
.date .m{background:var(--lime);font-size:8px;font-weight:700;color:var(--ink);height:11px;line-height:11px}
.date .d{background:var(--white);font-size:15px;font-weight:700;color:var(--ink);height:20px;line-height:20px}
.news-item .t{font-size:10.5px;font-weight:700;color:var(--ink)}
.news-item p{font-size:10px;line-height:13.5px;color:#555}
.footer-brand{left:880px;top:68px;width:200px;text-align:center}
.footer-brand .brand-dot{margin:0 auto 8px;width:34px;height:34px}
.footer-brand .brand-name{font-size:15px;line-height:17px;color:#555}
.social{display:flex;gap:8px;justify-content:center;margin-top:20px}
.social span{width:24px;height:24px;border-radius:50%;background:#555}
.copyright{top:2394px;left:0;width:1200px;height:38px;background:var(--lime);display:flex;align-items:center;justify-content:center;font-size:11.5px;color:var(--ink)}
</style>
</head>
<body>

<!-- contact strip -->
<div class="abs contact-strip mail">
  <svg width="14" height="10" viewBox="0 0 14 10"><rect x="0.5" y="0.5" width="13" height="9" fill="none" stroke="#2b2b2b"/><path d="M1 1l6 5 6-5" fill="none" stroke="#2b2b2b"/></svg>
  info@fahrzeugpreisfinder.com
</div>
<div class="abs contact-strip phone">
  <svg width="12" height="12" viewBox="0 0 12 12"><path d="M3 1l2 2.5-1.2 1.5a7 7 0 003.2 3.2L8.5 7 11 9l-1 2C5 11 1 7 1 2z" fill="#fff"/></svg>
  +49 (0) 3000 12 34 567
</div>

<!-- header -->
<div class="abs brand">
  <span class="brand-dot"></span>
  <span class="brand-name">FAHRZEUG<br>PREIS FINDER</span>
</div>
<div class="abs appointment">
  <span class="icon">
    <svg width="18" height="18" viewBox="0 0 18 18"><rect x="2" y="3" width="14" height="13" fill="none" stroke="#2b2b2b" stroke-width="1.6"/><path d="M2 7h14M6 1v4M12 1v4" stroke="#2b2b2b" stroke-width="1.6"/></svg>
  </span>
  <span class="label">Make An Appointment</span>
</div>

<nav class="abs main-nav">
  <ul>
    <li style="width:135px">HOME</li>
    <li style="width:128px">INFO</li>
    <li style="width:178px">AUTO VALUE</li>
    <li style="width:130px">CAR LIST</li>
    <li style="width:167px">IMPRINT</li>
    <li style="width:138px">TWEET</li>
  </ul>
</nav>

<!-- hero -->
<section class="abs hero">
  <div class="hero-photo" role="img" aria-label="Hand holding a car key in front of a white car"></div>
</section>
<div class="abs valuation"></div>
<div class="abs ribbon">
  <span class="tail l"></span><span class="tail r"></span>
  <div class="band">Free Evaluation Of Your Car<br>Immediately And Without Registration</div>
</div>
<div class="abs field-label" style="top:238px">Insert Offer URL To Comparable Car Here</div>
<div class="abs field" style="left:678px;top:259px;width:305px">Insert offer URL to comparable car here</div>
<div class="abs field-label" style="top:300px">Enter Your Vehicle Key</div>
<div class="abs field" style="left:678px;top:324px;width:148px">HSN</div>
<div class="abs field" style="left:835px;top:324px;width:148px">TSN</div>
<div class="abs field select" style="left:678px;top:375px;width:305px">Select Your Model
  <svg width="10" height="6" viewBox="0 0 10 6"><path d="M1 1l4 4 4-4" fill="none" stroke="#333" stroke-width="1.5"/></svg></div>
<div class="abs field select" style="left:678px;top:425px;width:305px">Select Your Brand
  <svg width="10" height="6" viewBox="0 0 10 6"><path d="M1 1l4 4 4-4" fill="none" stroke="#333" stroke-width="1.5"/></svg></div>
<div class="abs get-btn">GET FREE VALUATION</div>

<!-- car value -->
<section class="abs car-value" role="img" aria-label="Dark road scene with a car at dusk">
  <h2 class="section-title">The Car <span class="accent">Value</span></h2>
  <p>Who wants to buy a used car or sell his old car , does not come around it to make a realistic idea about the price . Often an objective evaluation of a used car is chargeable. But there is also free car value calculator or auto - lists can provide that the same benefits as a premium offerings . And of course with significantly fewer circumstances and time.</p>
  <span class="read-more">Read More »</span>
</section>

<!-- features -->
<section class="abs features">
  <div class="feature" style="left:188px">
    <div class="ring"><div class="core">
      <svg width="92" height="92" viewBox="0 0 92 92" role="img" aria-label="Free of charge badge"><circle cx="46" cy="46" r="42" fill="#5b6b1e"/><circle cx="46" cy="46" r="32" fill="none" stroke="#fff" stroke-width="2"/></svg>
    </div></div>
    <h3>100% Free<br>100% not binding</h3>
  </div>
  <div class="feature" style="left:480px">
    <div class="ring"><div class="core">
      <svg width="60" height="70" viewBox="0 0 60 70"><path d="M6 4h30l14 14v46H6z" fill="none" stroke="#5b6b1e" stroke-width="4"/><path d="M14 26h24M14 36h20M14 46h14" stroke="#5b6b1e" stroke-width="4"/><circle cx="44" cy="54" r="12" fill="#5b6b1e"/><path d="M39 49l10 10M49 49l-10 10" stroke="#fff" stroke-width="3"/></svg>
    </div></div>
    <h3>No Registration Or<br>Personal Data Needed</h3>
  </div>
  <div class="feature" style="left:772px">
    <div class="ring"><div class="core">
      <svg width="50" height="70" viewBox="0 0 50 70"><path d="M4 4h42M4 66h42" stroke="#5b6b1e" stroke-width="5"/><path d="M9 6c0 18 30 20 30 29S9 44 9 64h32c0-20-30-20-30-29s30-11 30-29z" fill="#5b6b1e"/></svg>
    </div></div>
    <h3>Immediately Answer<br>Online In Seconds Cheers</h3>
  </div>
</section>

<!-- sell -->
<section class="abs sell">
  <div class="sell-photo" role="img" aria-label="Rear view of a red sports car on a road"></div>
  <h2 class="section-title">How To Sell Your Car</h2>
  <h4>Work Out What It’s Worth With A Free Valuation</h4>
  <p>Lorem ipsum dolor sit amet, consectetuer adipiscing elit, sed diam nonummy nibh euismod tincidunt ut laoreet dolore magna aliquam erat volutpat. Ut wisi enim ad minim veniam, quis nostrud exerci tation ullamcorper suscipit lobortis nisl ut aliquip ex ea commodo consequat. Duis autem vel eum iriure dolor in hendrerit in vulputate velit esse molestie consequat, vel illum dolore eu feugiat nulla facilisis at vero eros et accumsan et iusto odio dignissim qui blandit praesent luptatum zzril delenit augue duis dolore te feugait nulla facilisi dolore magna aliquam erat volutpat. Ut wisi enim ad minim veniam, quis nostrud exerci tation ullamcorper suscipit lobortis nisl ut aliquip ex ea commodo consequat.</p>
  <span class="read-more">Read More »</span>
</section>

<!-- car list -->
<section class="abs car-list">
  <h2 class="section-title">Car <span class="accent">List</span></h2>
  <div class="make" style="left:162px;top:110px">Aldera</div>
  <div class="make" style="left:311px;top:110px">Kestrel</div>
  <div class="make" style="left:461px;top:110px">Corvane</div>
  <div class="make" style="left:611px;top:110px">Halden</div>
  <div class="make" style="left:760px;top:110px">Tesso</div>
  <div class="make" style="left:911px;top:110px">Marlow<br>Werke</div>
  <div class="make" style="left:162px;top:227px">Ostrand</div>
  <div class="make" style="left:311px;top:227px">Pavione</div>
  <div class="make" style="left:461px;top:227px">Rivane</div>
  <div class="make" style="left:611px;top:227px">Tamaro</div>
  <div class="make" style="left:760px;top:227px">Sorvik</div>
  <div class="make" style="left:911px;top:227px">Vendel</div>
</section>

<!-- reviews -->
<section class="abs reviews">
  <h2 class="section-title">Customer <span class="accent">Reviews</span></h2>
  <div class="arrow" style="left:106px"><svg width="10" height="8" viewBox="0 0 10 8"><path d="M9 4H1M4 1L1 4l3 3" fill="none" stroke="#fff" stroke-width="1.5"/></svg></div>
  <div class="arrow" style="left:1070px"><svg width="10" height="8" viewBox="0 0 10 8"><path d="M1 4h8M6 1l3 3-3 3" fill="none" stroke="#fff" stroke-width="1.5"/></svg></div>
  <article class="review" style="left:162px;width:419px">
    <div class="portrait" role="img" aria-label="Portrait photo of a customer" style="background:linear-gradient(160deg,#c9ced4,#2d3540)"></div>
    <div class="body">
      <p>Lorem ipsum dolor sit amet, consectetuerle adipiscing elit, sed diam nonummy nibhtatin euismod tincidunt ut laoreet dolore magna aliquam erat volutpat wisi enim ad minim veniam quis nostrud exerci tation.</p>
      <div class="stars">★★★★★</div>
      <div class="name">Lena Hartwig</div>
    </div>
  </article>
  <article class="review" style="left:626px;width:412px">
    <div class="portrait" role="img" aria-label="Portrait photo of a customer" style="background:linear-gradient(160deg,#d9b9a3,#8a3a2c)"></div>
    <div class="body">
      <p>Lorem ipsum dolor sit amet, consectetuerle adipiscing elit, sed diam nonummy nibhtatin euismod tincidunt ut laoreet dolore magna aliquam erat volutpat wisi enim ad minim veniam quis nostrud exerci tation.</p>
      <div class="stars">★★★★<span class="off">★</span></div>
      <div class="name">Jonas Keller</div>
    </div>
  </article>
</section>

<!-- footer -->
<footer class="abs site-footer">
  <div class="abs quick-links">
    <h5>Quick Links</h5>
    <ul><li>HOME</li><li>INFO</li><li>AUTO VALUE</li><li>CAR LIST</li><li>IMPRINT</li><li>TWEET</li></ul>
  </div>
  <div class="abs contact-info">
    <h5>Contact Information</h5>
    <div class="contact-row">
      <svg width="10" height="14" viewBox="0 0 10 14"><path d="M5 0a5 5 0 00-5 5c0 4 5 9 5 9s5-5 5-9a5 5 0 00-5-5z" fill="#acd036"/><circle cx="5" cy="5" r="2" fill="#ededed"/></svg>
      <span><b>FAHRZEUGPREISFINDER</b><br>123 euismod cidun ut laoreet laoreet dol magna aliquam</span>
    </div>
    <div class="contact-row" style="margin-top:20px">
      <svg width="12" height="12" viewBox="0 0 12 12"><path d="M3 1l2 2.5-1.2 1.5a7 7 0 003.2 3.2L8.5 7 11 9l-1 2C5 11 1 7 1 2z" fill="#acd036"/></svg>
      <span>+49 (0) 3000 12 34 567</span>
    </div>
    <div class="contact-row" style="margin-top:20px">
      <svg width="14" height="10" viewBox="0 0 14 10"><rect width="14" height="10" fill="#acd036"/><path d="M1 1l6 5 6-5" fill="none" stroke="#fff"/></svg>
      <span>info@fahrzeugpreisfinder.com</span>
    </div>
  </div>
  <div class="abs news">
    <h5>Latest News</h5>
    <div class="news-item">
      <div class="date"><div class="m">AUG</div><div class="d">09</div></div>
      <div><div class="t">Lorem ipsum dolor sit amet .</div><p>Lorem ipsum dol adipiscing elit, seder Dollar smit quis nostrud exerci tation adipiscing elit.</p></div>
    </div>
    <div class="news-item">
      <div class="date"><div class="m">AUG</div><div class="d">10</div></div>
      <div><div class="t">Lorem ipsum dolor sit amet .</div><p>Lorem ipsum dol adipiscing elit, seder or sit amet, consectetuer Dollar smit quis nostrud exerci tation elit.</p></div>
    </div>
  </div>
  <div class="abs footer-brand">
    <div class="brand-dot" style="background:#555"></div>
    <div class="brand-name">FAHRZEUG<br>PREIS FINDER</div>
    <div class="social" aria-label="Social media links"><span></span><span></span><span></span><span></span></div>
  </div>
</footer>
<div class="abs copyright">Copyright © 2016 FAHRZEUGPREISFINDER. All Rights Reserved.</div>

</body>
</html>
```